Brimvale Crest Homes needs a business card

We need a business card for a new company in Canada, Ontario. Our company is all about luxury contraction homes for our clients. Our product and services are custom projects design. Under the business logo that will be created, we want a slogan that will be a memorable phrase for consumers to remember us to tell their friends and relatives.

Additional infomation
- Teodoro Vanlesky
- President / Ceo
-519.304.7718

Find point what luxury construction products and services can be done

We like to see colors:
- #663300
- and something other colors or color that would attract the client needs and wants

The final design should communicate leads from new or old clients that will grow our empire. Most of all, we try to work among the budget that clients want

NOTE
- we also need an icon for the business (Example: Instagram, Facebook, and Whatsapp icons)
- We want the company name to be remembered easily for clients and our distributors who would get our orders.
- we need an icon on the business cards: Facebook and Instagram.

Thanks,
Brimvale Crest Homes

```html
<!DOCTYPE html>
<html lang="en">
<head>
<meta charset="utf-8">
<title>Brimvale Crest Homes – Business Card</title>
<link href="https://fonts.googleapis.com/css2?family=Open+Sans:wght@400;600&family=Roboto+Condensed:wght@400;700&display=swap" rel="stylesheet">
<style>
  :root {
    --backdrop: #2b2b2d;
    --card: #1b1c1e;
    --card-pattern-a: #1e1f21;
    --card-pattern-b: #26272a;
    --brand-brown: #663300;
    --name-brown: #8a4712;
    --ink-light: #f2f2f2;
    --rule: #7d7d80;
    --social-dot: #4a4b4f;
  }
  html, body {
    margin: 0;
    padding: 0;
    width: 1200px;
    height: 1108px;
    overflow: hidden;
    background: var(--backdrop);
  }
  .canvas {
    position: relative;
    width: 1200px;
    height: 1108px;
  }
  .card {
    position: absolute;
    top: 170px;
    width: 430px;
    height: 740px;
    border-radius: 26px;
    background: var(--card);
    overflow: hidden;
    box-shadow: 0 18px 40px rgba(0,0,0,0.45);
  }
  .card--front { left: 125px; }
  .card--back  { left: 645px; }

  /* Front */
  .brand {
    position: absolute;
    top: 205px;
    left: 0;
    right: 0;
    text-align: center;
    color: var(--brand-brown);
    font-family: "Roboto Condensed", sans-serif;
  }
  .brand__name {
    font-weight: 700;
    font-size: 40px;
    letter-spacing: 0.5px;
    line-height: 1;
  }
  .brand__slogan {
    margin-top: 8px;
    font-weight: 700;
    font-size: 13.5px;
    letter-spacing: 0.6px;
  }
  .contact {
    position: absolute;
    top: 440px;
    left: 0;
    right: 0;
    text-align: center;
    font-family: "Open Sans", sans-serif;
    color: var(--ink-light);
  }
  .contact__name {
    font-family: "Roboto Condensed", sans-serif;
    font-weight: 700;
    font-size: 30px;
    color: var(--name-brown);
    text-transform: uppercase;
    letter-spacing: 0.3px;
  }
  .contact__role {
    font-size: 22px;
    margin-top: 2px;
  }
  .contact__rule {
    width: 270px;
    height: 1px;
    margin: 14px auto;
    background: var(--rule);
  }
  .contact__phone {
    font-size: 27px;
    letter-spacing: 0.5px;
  }
  .social {
    position: relative;
    width: 270px;
    height: 34px;
    margin: 18px auto 0;
  }
  .social__line {
    position: absolute;
    top: 50%;
    left: 0;
    right: 0;
    height: 1px;
    background: var(--rule);
  }
  .social__dots {
    position: relative;
    display: flex;
    justify-content: center;
    gap: 8px;
  }
  .social__dot {
    width: 32px;
    height: 32px;
    border-radius: 50%;
    background: var(--social-dot);
  }

  /* Back */
  .back__pattern {
    position: absolute;
    inset: 0;
    background: linear-gradient(160deg, var(--card-pattern-b) 0%, var(--card-pattern-a) 70%, var(--card) 100%);
  }
  .back__wordmark {
    position: absolute;
    left: 40px;
    bottom: 85px;
    font-family: "Roboto Condensed", sans-serif;
    font-weight: 700;
    font-size: 38px;
    color: var(--ink-light);
  }
</style>
</head>
<body>
<main class="canvas">
  <section class="card card--front" aria-label="Business card front">
    <div class="brand">
      <div class="brand__name">Brimvale Crest Homes</div>
      <div class="brand__slogan">- HOME RENOVATIONS - CUSTOM PROJECT DESIGN -</div>
    </div>
    <div class="contact">
      <div class="contact__name">Teodoro Vanlesky</div>
      <div class="contact__role">President / CEO</div>
      <div class="contact__rule"></div>
      <div class="contact__phone">519.304.7718</div>
      <div class="social">
        <div class="social__line"></div>
        <div class="social__dots">
          <span class="social__dot"></span>
          <span class="social__dot"></span>
        </div>
      </div>
    </div>
  </section>

  <section class="card card--back" aria-label="Business card back">
    <div class="back__pattern" role="img" aria-label="Tonal repeating brand name pattern"></div>
    <div class="back__wordmark">Brimvale Crest Homes</div>
  </section>
</main>
</body>
</html>
```